Customer Paperwork Redesign

We need the following PDF redesigned to be more user friendly.
We are finding that
1. People are not setting up payments
2. People are not returning the paperwork with the bank information properly filled out.
3. The bank details are actually not used, they are only a backup. This needs to be made prominent. many people phone us about this.
4. People find it all too confusing. Perosnally i think its easy but hey.. im not our customer.
Let me know what you can do!
Content can be totaly rewritten,
This form gets automatically filled out by our software, printed and then mailed to them. They only need to sign, and fill out the bank details and return it. They also need to call up to setup payments.
The final tramvolo form can be redesigned however, how too much. eg, Locations of content should be fairly much the same.
Current document is attached. its the PDF.
I have also uploaded a logo, and a .doc which is handy to edit. Also have uploaded the tramvolo PDF too.
Target Market(s)
Our target market is people who dont have very good english skills, cant read well and need something really easy and simple to follow. Something thats to much effort becomes too hard
Industry/Entity Type
Bank

```html
<!DOCTYPE html>
<html lang="en">
<head>
<meta charset="utf-8">
<title>Hire Agreement</title>
<link href="https://fonts.googleapis.com/css2?family=Source+Sans+3:ital,wght@0,400;0,600;0,700;1,600&display=swap" rel="stylesheet">
<style>
:root{
  --backdrop:#d9d9d9;
  --paper:#ffffff;
  --ink:#1a1a1a;
  --muted:#a7a7a7;
  --brand:#2b86c5;
  --brand-dark:#1f6fab;
  --field:#eef6fb;
  --field-line:#a9cbe3;
}
*{box-sizing:border-box;margin:0;padding:0}
html,body{width:877px;height:1200px;overflow:hidden}
body{background:var(--backdrop);font-family:"Source Sans 3",Arial,sans-serif;color:var(--ink);position:relative}
.page{position:absolute;left:57px;top:31px;width:760px;height:1101px;background:var(--paper);box-shadow:0 2px 10px rgba(0,0,0,.25)}
.page > *{position:absolute}
.keep-note{left:138px;top:72px;font-size:17px;color:var(--muted)}
.brand{left:405px;top:62px;display:flex;align-items:center;gap:10px}
.brand-dot{width:40px;height:40px;border-radius:50%;background:var(--brand)}
.brand-name{font-size:30px;font-weight:600;color:var(--brand);line-height:1}
.brand-tag{font-size:11px;font-weight:600;color:var(--brand);margin-top:3px}
.date-line{left:58px;top:147px;display:flex;align-items:center;font-size:14px;gap:6px}
.date-line b{font-weight:700}
.field{background:var(--field);border:1px solid var(--field-line);height:25px}
.between{left:58px;top:186px;font-size:13px;font-weight:700;color:var(--brand)}
.parties{left:58px;top:222px;font-size:13.5px;line-height:17px}
.lessee-box{left:104px;top:258px;width:264px;height:24px}
.clause{left:79px;width:624px;display:flex;gap:12px;font-size:8.6px;line-height:11.6px;text-align:justify}
.num{flex:none;width:14px;height:14px;border-radius:50%;background:var(--brand);color:#fff;font-size:8px;font-weight:700;display:flex;align-items:center;justify-content:center}
.schedule-bar{left:58px;top:842px;width:646px;height:24px}
.schedule-tab{position:absolute;left:0;top:0;width:154px;height:24px;background:var(--brand-dark);color:#fff;font-size:16px;font-weight:700;padding-left:14px;line-height:24px}
.schedule-rule{position:absolute;left:0;right:0;bottom:0;height:4px;background:var(--brand)}
.schedule-row{left:80px;display:flex;align-items:center;gap:12px}
.schedule-row label{width:232px;text-align:right;font-size:14px;font-weight:600;font-style:italic}
.schedule-row .field{width:272px;height:25px}
.signature{left:58px;top:1035px;width:310px;border-top:1px solid #333}
.foot-band{left:0;bottom:0;width:100%;height:12px;background:var(--brand)}
</style>
</head>
<body>
<main class="page">
  <p class="keep-note">You keep this page</p>
  <div class="brand">
    <span class="brand-dot"></span>
    <div>
      <div class="brand-name">DeskShare</div>
      <div class="brand-tag">Helping families get connected at home</div>
    </div>
  </div>

  <div class="date-line"><b>THIS AGREEMENT</b> is made the day <span class="field" style="width:51px"></span> of <span class="field" style="width:84px"></span> 20 <span class="field" style="width:51px"></span></div>
  <p class="between">BETWEEN:</p>
  <p class="parties">LOAN FOR LAPTOPS PTY. LTD. ACN 402 718 306 of 4/8 Kellan St in the State of Victoria<br>(hereinafter called “the Hirer”)<br>- and -</p>
  <span class="field lessee-box"></span>

  <div class="clause" style="top:304px"><span class="num">1</span><p>The Hirer is hiring the computer noted in the First Schedule of this Agreement to the Lessee who is renting the computer from the Hirer. The Hirer agrees that he/she has satisfied himself/herself as to the condition and suitability of the computer and has not been induced to enter into this agreement by any statement made by the Hirer or its representatives which is not included in this agreement.</p></div>
  <div class="clause" style="top:352px"><span class="num">2</span><p>The hire fee is the amount shown in the First Schedule of this agreement and will be paid monthly in advance with the first payment to be made on this date. The Lessee gives an irrevocable authority to the Hirer for the deduction of all rental payments under this agreement to Benefitline and/or the Department of Family Support to make all payments under the terms of this agreement to the Hirer. The Lessee understands that the hire fee is paid even in the unfortunate circumstance that a dispute occurs between himself/herself and the Hirer.</p></div>
  <div class="clause" style="top:417px"><span class="num">3</span><p>The Lessee must make the number of payments shown in the Schedule on the dates shown in the Schedule.</p></div>
  <div class="clause" style="top:437px"><span class="num">4</span><p>Ownership in the computer remains with the Hirer until the end of the period of the Lease. At that time and provided that all payments have been made in accordance with this agreement then ownership of the computer transfers to the Lessee.</p></div>
  <div class="clause" style="top:474px"><span class="num">5</span><p>If the Lessee benefit from Benefitline is discontinued then all further payments which are due under the terms of this agreement become immediately due and payable and must be paid within fourteen (14) days of the date of the discontinuance of payment.</p></div>
  <div class="clause" style="top:508px"><span class="num">6</span><p>The ownership of the computer will not transfer to the Hirer in the circumstance described in Clause 5 above until all payments have been made.</p></div>
  <div class="clause" style="top:545px"><span class="num">7</span><p>The Hirer warrants to the Lessee that the Lessee will have peaceful possession and enjoyment of the computer during the rental period provided that the hire fee is duly and punctually paid in accordance with the terms of this agreement.</p></div>
  <div class="clause" style="top:585px"><span class="num">8</span><p>The Lessee warrants to the Hirer that he/she has the right and authority to enter into and complete the terms of this agreement. The information supplied by the Lessee to the Hirer is true and correct and no relevant information has been omitted. The Lessee understands that if he/she fails to meet his/her payment obligations under this agreement then the Hirer can collect the computer from the Lessee with or without any notice and that this agreement is terminated. In the circumstance that any damage has been done to the computer then the Hirer is responsible for the cost of repair of that damage. The fact that the hirer has collected the computer does not mean that the Lessee’s responsibility for payment has ended. The opposite is the case. The Lessee remains responsible to make all payments for the computer and is expected to make such payments. The Lessee understands that the Hirer will take any action that it considers appropriate to recover the money that remains unpaid or the cost of repair for the damage done to the computer.</p></div>
  <div class="clause" style="top:694px"><span class="num">9</span><p>In the circumstance that any taxes or stamp duty needs to be paid by State or Federal Law then the Hirer will advise the Lessee of the amount of that tax or stamp duty. The payment for the tax or stamp duty will be paid by the Lessee to the Hirer on the date that the first rental payment is made. It will then be the Hirer’s responsibility to pay the tax or the stamp duty to the appropriate authority.</p></div>
  <div class="clause" style="top:743px"><span class="num">10</span><p>The parties confirm that the Hirer has asked the Lessee to obtain legal advice about this agreement. The Lessee has made his/her own decision whether to accept that request. In any event, this agreement has been signed freely and voluntarily by the Lessee without any pressure from the Hirer or from any third party. The Lessee confirms his/her understanding of the terms of the agreement whether legal advice has been received or not received.</p></div>
  <div class="clause" style="top:805px"><span class="num">11</span><p>Wheresoever’s appropriate and where the context of this agreement permits words importing the singular number or the feminine gender will be read as importing the plural number or extending to males and vice versa.</p></div>

  <div class="schedule-bar"><span class="schedule-rule"></span><span class="schedule-tab">Schedule</span></div>
  <div class="schedule-row" style="top:878px"><label>Lessee’s Name:</label><span class="field"></span></div>
  <div class="schedule-row" style="top:905px"><label>Computer Description:</label><span class="field"></span></div>
  <div class="schedule-row" style="top:932px"><label>Payment Arrangements:</label><span class="field"></span></div>

  <div class="signature"></div>
  <div class="foot-band"></div>
</main>
</body>
</html>
```